Brinq - Web Design Rebrand for Manufacturing Automation Company

I need a new brand for a customer based in Ireland.
The website currently: https://corvexsystems.com/
Corvex Automation provides a wide range of automation and IT solutions used in manufacturing operations.
Their solutions span a broad spectrum of technology from physical machines and robots to cloud based management solutions for these systems.
They are an Authorised Distributor for Tarnfield Automation.
Their partnership with Tarnfield Automation will now include working closely to keep track of supply trends and preparing customers for future Data Centre projects.

Essentially their USP:
They have a large team of specialist technical people spanning the breadth of skills to be able to deploy and support automation and IT solutions in manufacturing in the Life Sciences Industry.

Along with Tarnfield Automation, they have specialist teams for accelerating Data Center applications.

Competitor websites:
https://www.valtriq.com/global/en.html - I really like the layout of their partnerships/collaborations section.
https://global.kmo/group/en - Their first moving imagery/tagline and 'discover more' when you enter the site is really eye-catching.
https://www.dp.com/uk/en/ - They layout and structure of the 'The core of what we do section' is really nice.

These are a big companies so anything we could steal would be good 😊

They want:
• Fresh, sharp imagery
• Movement on the main page and perhaps video on some sections? - similar to KMO
• A page to showcase Automation Solutions
• A page to showcase Data Centers
• About us
• Sectors they operate in (includes Life Sciences, Food & Bev, Data Centres)

Industry/Entity Type

Life Science Manufacturing

Number of Pages Required

1 page

Font styles to use
Sans Serif

Colors
0054AA
0677BA
7BADD7
CADEEF
E8F1F8

Requirements
Must have
• Moving Imagery

```html
<!DOCTYPE html>
<html lang="en">
<head>
<meta charset="utf-8">
<title>Corvex Automation</title>
<link href="https://fonts.googleapis.com/css2?family=Teko:wght@500;600&family=Montserrat:wght@400;500;600;700&display=swap" rel="stylesheet">
<style>
:root{
  --blue-deep:#0054AA;
  --blue:#0677BA;
  --blue-mid:#7BADD7;
  --blue-pale:#CADEEF;
  --blue-mist:#E8F1F8;
  --nav:#0AA3EA;
  --ink:#1a1a1a;
  --text:#4a4a4a;
  --navy:#0D2B63;
  --navy-dark:#0A2352;
  --grey:#F5F5F5;
  --white:#fff;
}
*{box-sizing:border-box;margin:0;padding:0}
html,body{width:1200px;height:3005px;overflow:hidden}
body{font-family:'Montserrat',sans-serif;color:var(--text);background:var(--white);position:relative}
.abs{position:absolute}
/* header */
.topbar{left:0;top:0;width:1200px;height:98px;background:var(--blue-mist)}
.brand{left:234px;top:26px;display:flex;align-items:center;gap:10px;font-weight:600;font-size:14px;letter-spacing:.5px;color:var(--blue)}
.brand-mark{width:26px;height:26px;background:var(--blue);border-radius:3px}
.social{display:flex;gap:8px}
.social span{width:32px;height:32px;border:1.5px solid var(--blue-deep);border-radius:50%;display:block}
.topbar .social{position:absolute;left:856px;top:23px}
.mainnav{left:234px;top:78px;width:731px;height:42px;background:var(--nav);border-radius:3px;display:flex;align-items:center;padding:0 18px;gap:30px;z-index:3}
.mainnav a{color:var(--white);text-decoration:none;font-size:13px;font-weight:500}
.mainnav .search{margin-left:auto}
/* hero */
.hero{left:0;top:98px;width:1200px;height:580px;background:radial-gradient(ellipse at 75% 35%,#5f8ed0 0%,#2f5fae 35%,#1a3f86 70%,#15356f 100%)}
.hero-text{left:234px;top:240px;color:var(--white)}
.hero h1{font-family:'Teko',sans-serif;font-weight:600;font-size:58px;line-height:51px;letter-spacing:.5px;text-transform:uppercase}
.hero p{font-size:15px;line-height:19px;width:420px;margin-top:22px}
.btn{display:inline-block;background:var(--blue-deep);color:var(--white);font-size:12px;font-weight:600;text-transform:uppercase;letter-spacing:.4px;text-decoration:none;border-radius:3px}
.hero .btn{margin-top:24px;padding:14px 24px}
.hero-wave{left:0;top:620px;width:1200px;height:60px}
/* headings */
.sec-title{left:0;width:1200px;text-align:center;font-family:'Teko',sans-serif;font-weight:600;font-size:48px;letter-spacing:7px;color:var(--ink);text-transform:uppercase;line-height:1}
.sec-title em{font-style:normal;color:var(--blue)}
.sec-title::after{content:"";display:block;width:72px;height:3px;background:var(--blue);margin:6px auto 0}
/* about */
.about-photo{left:234px;top:817px;width:294px;height:355px;background:linear-gradient(160deg,#c9d2dc,#8c98a6 50%,#5d6773)}
.about-copy{left:571px;top:815px;width:394px;font-size:11px;line-height:19px}
.about-copy p{margin-bottom:12px}
.about-copy .btn{margin-top:8px;padding:10px 18px;font-size:11px}
/* tiles */
.tile{position:absolute;overflow:hidden;border:1px solid rgba(255,255,255,.35)}
.tile .cap{position:absolute;left:16px;bottom:16px;padding-left:0;color:var(--white)}
.tile .cap::before{content:"";position:absolute;left:-16px;top:2px;width:4px;height:calc(100% - 4px);background:var(--blue)}
.tile h3{font-size:16px;font-weight:700;line-height:20px}
.tile p{font-size:11px;line-height:16px;font-weight:500}
/* partners */
.partners{left:0;top:2133px;width:1200px;height:410px;background:var(--blue-deep)}
.partners .sec-title{color:var(--white)}
.partners .sec-title::after{background:var(--white)}
.pcard{position:absolute;background:var(--white);display:flex;align-items:center;justify-content:center;gap:18px;font-size:13px;font-weight:600;color:#c8ccd2}
.pcard.active{background:var(--blue-pale);color:var(--ink)}
.pcard .sep{width:1px;height:32px;background:currentColor;opacity:.5}
.pcard .go{position:absolute;left:50%;bottom:16px;transform:translateX(-50%);width:34px;height:16px;border-radius:8px;background:var(--blue-deep)}
.arrow{position:absolute;width:28px;height:28px}
/* customers */
.customers{left:0;top:2525px;width:1200px;height:320px;background:var(--grey)}
.clogo{position:absolute;top:2686px;width:137px;height:81px;background:var(--white);display:flex;align-items:center;justify-content:center;font-size:15px;font-weight:600;color:#333}
/* footer */
.footer{left:0;top:2843px;width:1200px;height:135px;background:var(--navy)}
.footer .brand{position:absolute;left:406px;top:30px;color:var(--blue)}
.footer .social{position:absolute;left:684px;top:26px}
.footer .social span{border-color:var(--white)}
.footnav{position:absolute;left:0;width:1200px;top:98px;display:flex;justify-content:center;gap:28px}
.footnav a{color:var(--white);font-size:11.5px;text-decoration:none}
.legal{left:0;top:2978px;width:1200px;height:27px;background:var(--navy-dark);color:var(--blue-pale);font-size:11px;text-align:center;line-height:27px}
</style>
</head>
<body>

<header class="abs topbar">
  <div class="abs brand" style="top:26px"><span class="brand-mark"></span>CORVEX AUTOMATION</div>
  <div class="social" aria-label="Social profiles"><span></span><span></span><span></span></div>
</header>
<nav class="abs mainnav">
  <a href="#">Robotics And Automation Solutions</a><a href="#">Data Centers</a><a href="#">About Us</a><a href="#">Contact</a>
  <svg class="search" width="15" height="15" viewBox="0 0 15 15" fill="none" stroke="#fff" stroke-width="1.5"><circle cx="6.5" cy="6.5" r="5"/><path d="M10.2 10.2L14 14"/></svg>
</nav>

<section class="abs hero" role="img" aria-label="Blue robotic arm against a glowing network of connected points"></section>
<svg class="abs hero-wave" viewBox="0 0 1200 60" preserveAspectRatio="none">
  <path d="M0 14 L600 46 L1200 14 L1200 60 L0 60Z" fill="#fff"/>
  <path d="M0 14 L600 46 L1200 14 L1200 26 L600 54 L0 26Z" fill="#CADEEF"/>
</svg>
<div class="abs hero-text">
  <h1>Your Automation,<br>IT and Data Centre<br>Solutions Provider</h1>
  <p>A Tarnfield Automation Distributor Specialising in Life Sciences and Data Centres.</p>
  <a class="btn" href="#">Contact Us</a>
</div>

<h2 class="abs sec-title" style="top:728px"><em>About</em> Corvex Automation</h2>
<div class="abs about-photo" role="img" aria-label="Engineers in hard hats reviewing a production line"></div>
<div class="abs about-copy">
  <p>Corvex Automation provides a wide range of automation and IT solutions used in manufacturing operations.</p>
  <p>Our solutions span a broad spectrum of technology from physical machines and robots to cloud based management solutions for these systems.</p>
  <p>Along with Tarnfield Automation, we work closely to keep track of supply trends and invest wisely to prepare for customers' future DC projects.</p>
  <p>We have a large team of specialist technical people spanning the breadth of skills to be able to deploy and support these technologies.</p>
  <p>Authorised Distributor for Tarnfield Automation (Keller Drives and Safehold are Tarnfield Automation brands)</p>
  <p>Orvane Robotics Solutions' official distributor</p>
  <a class="btn" href="#">Read More</a>
</div>

<h2 class="abs sec-title" style="top:1240px"><em>Robotics</em> and Automation Solutions</h2>

<div class="tile" style="left:0;top:1329px;width:480px;height:268px;background:linear-gradient(135deg,#0c2a5c,#1f5fae 50%,#0a1f45)" role="img" aria-label="Glowing server stack on a circuit board"><div class="cap"><h3>Data Architecture</h3><p>Enterprise data architecture</p></div></div>
<div class="tile" style="left:480px;top:1329px;width:240px;height:268px;background:linear-gradient(160deg,#d4dfe4,#8fa3ad 60%,#5b6b75)" role="img" aria-label="Laptop showing production charts"><div class="cap"><h3>Data Historian</h3><p>Production data solutions</p></div></div>
<div class="tile" style="left:720px;top:1329px;width:480px;height:268px;background:linear-gradient(135deg,#071a3e,#1a4f96 55%,#3f86d1)" role="img" aria-label="Hand touching a digital data interface"><div class="cap"><h3>GxP Data Integrity</h3><p>GxP Data solutions &amp; services</p></div></div>

<div class="tile" style="left:0;top:1597px;width:240px;height:268px;background:linear-gradient(150deg,#cfe3ee,#4f8fb7 55%,#163f6a)" role="img" aria-label="Analytics icons around a globe"><div class="cap"><h3>KPIs &amp; Analytics</h3><p>Putting information in the hands<br>of decision makers</p></div></div>
<div class="tile" style="left:240px;top:1597px;width:240px;height:268px;background:linear-gradient(160deg,#1f3452,#3d5f86 55%,#1a2a40)" role="img" aria-label="Engineer with a laptop in a facility"><div class="cap"><h3>Legacy Systems</h3><p>Solutions and service for legacy<br>technology</p></div></div>
<div class="tile" style="left:480px;top:1597px;width:480px;height:268px;background:linear-gradient(120deg,#1d2f4d,#3b5577 50%,#8a6a55)" role="img" aria-label="Technician working at network racks"><div class="cap"><h3>Industrial Networks</h3><p>Network &amp; Security solutions<br>and services</p></div></div>
<div class="tile" style="left:960px;top:1597px;width:240px;height:268px;background:linear-gradient(160deg,#cdd6dd,#8b9aa6 55%,#4a5865)" role="img" aria-label="Engineers inspecting machine wiring"><div class="cap"><h3>Machine Safety</h3><p>Functional Machine safety<br>products &amp; services</p></div></div>

<div class="tile" style="left:0;top:1865px;width:480px;height:268px;background:linear-gradient(135deg,#0b1e40,#22477f 55%,#7a3a2a)" role="img" aria-label="Network of data and cloud icons"><div class="cap"><h3>Manufacturing Database</h3><p>Manufacturing data solutions<br>&amp; services</p></div></div>
<div class="tile" style="left:480px;top:1865px;width:240px;height:268px;background:linear-gradient(160deg,#c7d2dc,#7d8e9c 55%,#3e4a55)" role="img" aria-label="Engineer beside a vehicle assembly"><div class="cap"><h3>Motor Control</h3><p>Induction motor control products<br>&amp; services</p></div></div>
<div class="tile" style="left:720px;top:1865px;width:240px;height:268px;background:linear-gradient(160deg,#b9c3c9,#6c7c70 55%,#2f3a36)" role="img" aria-label="Industrial robot cell with operator"><div class="cap"><h3>Robotics &amp; Mechatronics</h3><p>Mechatronics solutions<br>&amp; services</p></div></div>
<div class="tile" style="left:960px;top:1865px;width:240px;height:268px;background:linear-gradient(160deg,#e2e6ea,#9aa5ae 55%,#4e5a66)" role="img" aria-label="Group training session at a workbench"><div class="cap"><h3>Training</h3><p>Online and in person training<br>solutions</p></div></div>

<section class="abs partners">
  <h2 class="abs sec-title" style="top:68px">Corvex Technology Partners</h2>
</section>
<svg class="abs" style="left:0;top:2510px" width="1200" height="36" viewBox="0 0 1200 36" preserveAspectRatio="none"><path d="M0 0 L1200 0 L1200 14 L600 32 L0 14Z" fill="#0054AA"/></svg>
<svg class="arrow" style="left:188px;top:2358px" viewBox="0 0 28 28" fill="none" stroke="#fff" stroke-width="1.5"><circle cx="14" cy="14" r="12.5"/><path d="M20 14H8M12 10l-4 4 4 4"/></svg>
<div class="pcard" style="left:234px;top:2302px;width:228px;height:141px">CORVEX<span class="sep"></span>Modwave</div>
<div class="pcard active" style="left:472px;top:2297px;width:256px;height:151px">CORVEX<span class="sep"></span>Linqara<span class="go"></span></div>
<div class="pcard" style="left:737px;top:2302px;width:228px;height:141px">CORVEX<span class="sep"></span>Orvane</div>
<svg class="arrow" style="left:984px;top:2358px" viewBox="0 0 28 28" fill="none" stroke="#fff" stroke-width="1.5"><circle cx="14" cy="14" r="12.5"/><path d="M8 14h12M16 10l4 4-4 4"/></svg>

<section class="abs customers">
  <h2 class="abs sec-title" style="top:72px"><em>Our</em> Customers</h2>
</section>
<svg class="arrow" style="left:188px;top:2712px" viewBox="0 0 28 28" fill="none" stroke="#0677BA" stroke-width="1.5"><circle cx="14" cy="14" r="12.5"/><path d="M20 14H8M12 10l-4 4 4 4"/></svg>
<div class="clogo" style="left:234px">Pellvia</div>
<div class="clogo" style="left:383px">Marketon</div>
<div class="clogo" style="left:531px">Quince</div>
<div class="clogo" style="left:680px">Stellagen</div>
<div class="clogo" style="left:828px;font-size:12px">Halbrook Pharma</div>
<svg class="arrow" style="left:984px;top:2712px" viewBox="0 0 28 28" fill="none" stroke="#0677BA" stroke-width="1.5"><circle cx="14" cy="14" r="12.5"/><path d="M8 14h12M16 10l4 4-4 4"/></svg>

<footer class="abs footer">
  <div class="brand"><span class="brand-mark"></span>CORVEX AUTOMATION</div>
  <div class="social" aria-label="Social profiles"><span></span><span></span><span></span></div>
  <nav class="footnav"><a href="#">Robotics And Automation Solutions</a><a href="#">Data Centers</a><a href="#">About Us</a><a href="#">Contact</a></nav>
</footer>
<div class="abs legal">© 2024 Corvex Automation | All Rights Reserved</div>

</body>
</html>
```